Packaging Design job - Natural Sleep Aid Supplement

We need a packaging design theme for a Natural Sleep Aid Supplement allowing a fall asleep fast and a good quality of sleep. This product will be in blister form of 15 capsules. We need for this a packaging design for the box.Dimensions: 75 * 25 * 116 mmThe active ingredients are: passionflower; lemon balm and valerianProduct Name: SOMNATWe would like to see clean, modern and fresh designs.This should give the impression of professional products of pharmaceutical quality.You will also find attached the logo of our company.Ps : You can change the color of the logo

Font styles to use
Serif
Sans Serif

Colors

Designer to choose colors to be used in the design.

Requirements
Should not have
• Sales and other "must buy" "guaranteed" etc

```html
<!DOCTYPE html>
<html lang="en">
<head>
<meta charset="utf-8">
<title>DORVELIA – Natural Sleep Aid Supplement Box Dieline</title>
<link rel="stylesheet" href="https://fonts.googleapis.com/css2?family=Open+Sans:wght@600;700;800&display=swap">
<style>
  :root {
    --backdrop: #d3e1e9;
    --paper: #ffffff;
    --navy: #12306f;
    --deep-blue: #173f86;
    --bright-blue: #1a7fc0;
    --silver-light: #f2f2f2;
    --silver-mid: #cfcfd0;
    --ink: #12306f;
    --tagline: #8a8f96;
  }
  html, body {
    margin: 0;
    padding: 0;
    width: 767px;
    height: 1200px;
    overflow: hidden;
    background: var(--backdrop);
    font-family: "Open Sans", Arial, sans-serif;
  }
  .dieline {
    position: absolute;
    left: 0;
    top: 110px;
    width: 767px;
    height: 970px;
    display: block;
  }
  .paper { fill: var(--paper); }
  .stop-navy { stop-color: var(--navy); }
  .stop-deep { stop-color: var(--deep-blue); }
  .stop-bright { stop-color: var(--bright-blue); }
  .stop-silver-light { stop-color: var(--silver-light); }
  .stop-silver-mid { stop-color: var(--silver-mid); }
  .product-name {
    fill: var(--paper);
    font-weight: 800;
    letter-spacing: 0.5px;
  }
  .ingredient {
    fill: var(--ink);
    font-weight: 700;
  }
  .band-label {
    fill: var(--paper);
    font-weight: 700;
    font-size: 11px;
  }
  .brand-name {
    fill: var(--deep-blue);
    font-weight: 800;
  }
  .brand-dot { fill: var(--bright-blue); }
  .brand-tagline {
    fill: var(--tagline);
    font-weight: 600;
  }
  .badge-count, .badge-unit {
    fill: var(--paper);
    font-weight: 700;
  }
</style>
</head>
<body>
<svg class="dieline" viewBox="140 530 700 885" xmlns="http://www.w3.org/2000/svg" aria-label="Flat box layout for DORVELIA sleep aid supplement">
  <defs>
    <linearGradient id="blue-sweep" x1="0" y1="0" x2="1" y2="0">
      <stop offset="0" class="stop-navy"/>
      <stop offset="0.55" class="stop-deep"/>
      <stop offset="1" class="stop-bright"/>
    </linearGradient>
    <linearGradient id="band-sweep" x1="0" y1="0" x2="1" y2="0">
      <stop offset="0" class="stop-navy"/>
      <stop offset="0.5" class="stop-bright"/>
      <stop offset="1" class="stop-navy"/>
    </linearGradient>
    <linearGradient id="side-sweep" x1="0" y1="0" x2="1" y2="0">
      <stop offset="0" class="stop-navy"/>
      <stop offset="1" class="stop-bright"/>
    </linearGradient>
    <linearGradient id="silver-strip" x1="0" y1="0" x2="1" y2="0">
      <stop offset="0" class="stop-silver-mid"/>
      <stop offset="0.5" class="stop-silver-light"/>
      <stop offset="1" class="stop-silver-mid"/>
    </linearGradient>

    <!-- main panel artwork, 477 x 311 -->
    <g id="main-panel">
      <g class="brand-lockup">
        <circle class="brand-dot" cx="150" cy="36" r="11"/>
        <text class="brand-name" x="168" y="47" font-size="30">LUNAVERA</text>
        <text class="brand-tagline" x="182" y="62" font-size="7">NATURAL SLEEP &amp; WELLNESS LABORATORY</text>
      </g>
      <path d="M0 98 H435 C412 150 398 186 360 193 H0 Z" fill="url(#blue-sweep)"/>
      <text class="product-name" x="16" y="171" font-size="52">DORVELIA</text>
      <rect x="0" y="196" width="350" height="35" fill="url(#silver-strip)"/>
      <text class="ingredient" x="15" y="218" font-size="14">PASSIONFLOWER</text>
      <text class="ingredient" x="158" y="218" font-size="14">LEMON BALM</text>
      <text class="ingredient" x="273" y="218" font-size="14">VALERIAN</text>
      <g class="capsule-badge" transform="translate(435 213)">
        <polygon points="-13,-22 13,-22 26,0 13,22 -13,22 -26,0" fill="url(#side-sweep)"/>
        <text class="badge-count" x="0" y="0" font-size="13" text-anchor="middle">15</text>
        <text class="badge-unit" x="0" y="11" font-size="8" text-anchor="middle">capsules</text>
      </g>
      <rect x="0" y="270" width="477" height="41" fill="url(#band-sweep)"/>
      <text class="band-label" x="238" y="295" text-anchor="middle">NATURAL SLEEP AID SUPPLEMENT</text>
    </g>

    <!-- tuck flap artwork -->
    <g id="flap-panel">
      <path d="M0 0 H268 C255 30 245 52 220 57 H0 Z" fill="url(#blue-sweep)"/>
      <text class="product-name" x="10" y="43" font-size="32">DORVELIA</text>
      <rect x="0" y="59" width="192" height="18" fill="url(#silver-strip)"/>
      <text class="ingredient" x="8" y="71" font-size="8">PASSIONFLOWER</text>
      <text class="ingredient" x="88" y="71" font-size="8">LEMON BALM</text>
      <text class="ingredient" x="151" y="71" font-size="8">VALERIAN</text>
      <circle class="brand-dot" cx="302" cy="23" r="7"/>
      <text class="brand-name" x="313" y="30" font-size="19">LUNAVERA</text>
      <text class="brand-tagline" x="322" y="40" font-size="5">NATURAL SLEEP &amp; WELLNESS LABORATORY</text>
      <g transform="translate(455 63)">
        <polygon points="-8,-14 8,-14 16,0 8,14 -8,14 -16,0" fill="url(#side-sweep)"/>
        <text class="badge-count" x="0" y="1" font-size="9" text-anchor="middle">15</text>
        <text class="badge-unit" x="0" y="8" font-size="5" text-anchor="middle">capsules</text>
      </g>
    </g>
  </defs>

  <!-- die shapes -->
  <path class="paper" d="M253 537 H805 Q833 537 833 565 V820 Q833 848 805 848 H253 Z"/>
  <path class="paper" d="M225 848 H760 V930 Q760 950 740 950 H245 Q225 950 225 930 Z"/>
  <path class="paper" d="M170 952 H730 V1262 H170 Q147 1262 147 1239 V975 Q147 952 170 952 Z"/>
  <path class="paper" d="M220 1262 H760 V1365 Q745 1365 725 1390 Q712 1405 690 1405 H290 Q268 1405 255 1390 Q235 1365 220 1365 Z"/>

  <!-- front panel -->
  <use href="#main-panel" x="253" y="537"/>

  <!-- right side panel -->
  <g class="side-panel-right">
    <path d="M730 580 Q790 595 790 640 V848 H730 Z" fill="url(#side-sweep)"/>
    <rect x="790" y="645" width="16" height="195" fill="url(#silver-strip)"/>
    <text class="product-name" font-size="38" transform="translate(775 840) rotate(-90)">DORVELIA</text>
    <text class="ingredient" font-size="8" transform="translate(801 838) rotate(-90)">PASSIONFLOWER</text>
    <text class="ingredient" font-size="8" transform="translate(801 760) rotate(-90)">LEMON BALM</text>
    <text class="ingredient" font-size="8" transform="translate(801 695) rotate(-90)">VALERIAN</text>
  </g>

  <!-- top tuck flap -->
  <use href="#flap-panel" x="253" y="868"/>

  <!-- back panel -->
  <use href="#main-panel" x="250" y="952"/>

  <!-- left side panel -->
  <g class="side-panel-left">
    <path d="M190 952 H250 V1220 Q190 1205 190 1160 Z" fill="url(#side-sweep)"/>
    <rect x="174" y="958" width="16" height="185" fill="url(#silver-strip)"/>
    <text class="product-name" font-size="38" transform="translate(206 960) rotate(90)">DORVELIA</text>
    <text class="ingredient" font-size="8" transform="translate(179 962) rotate(90)">PASSIONFLOWER</text>
    <text class="ingredient" font-size="8" transform="translate(179 1038) rotate(90)">LEMON BALM</text>
    <text class="ingredient" font-size="8" transform="translate(179 1102) rotate(90)">VALERIAN</text>
  </g>

  <!-- bottom tuck flap -->
  <use href="#flap-panel" x="253" y="1282"/>
</svg>
</body>
</html>
```